Paper Towel Design - comparable to Plenzo, Quirtle, Dovrine, Moko

1.I needed a design for a new product, PAPER TOWEL
2. Name: FLORAMIST (Trademark)
3. One word with letters TM for a trademark at the end of the name
4. Include: SNIP-N-WIPE this pertains to sheet size of 11 inches x 6 inches
5. Include: 100 percent biodegradable
6. Include: STRONG & ABSORBENT
7. Include the words Paper Towel

Pavlo Market(s)

Household, store, businesses (Online, Hubbick, Zentro, Pavlo)

Industry/Entity Type

Paper Product

Font styles to use
Script

Colors
6b449b
33a6d7
fbee3e

Requirements
Must have
• vibrant color - striking design
Nice to have
• Excellent color combination of cyan, yellow, and purple
Should not have
• Should not be suggestive of any similar product, it should be unique and has its own identity

```html
<!DOCTYPE html>
<html lang="en">
<head>
<meta charset="utf-8">
<title>Floramist Paper Towels – Pack Front</title>
<link href="https://fonts.googleapis.com/css2?family=Lobster&family=Baloo+2:wght@600;700;800&display=swap" rel="stylesheet">
<style>
  :root {
    --pack-white: #f7f8f8;
    --brand-purple: #6b449b;
    --brand-purple-deep: #4e2f78;
    --brand-cyan: #33a6d7;
    --brand-cyan-deep: #1f86b5;
    --brand-yellow: #fbee3e;
    --brand-yellow-soft: #fdf6a6;
    --seam-grey: #e3e5e8;
    --badge-ring: #ffffff;
  }
  html, body {
    margin: 0;
    padding: 0;
    width: 1200px;
    height: 1200px;
    overflow: hidden;
    background: var(--pack-white);
  }
  .pack-front {
    position: relative;
    width: 1200px;
    height: 1200px;
    background: var(--pack-white);
    overflow: hidden;
  }
  .art-layer {
    position: absolute;
    inset: 0;
  }
  .brand-block {
    position: absolute;
    left: 600px;
    top: 370px;
    width: 580px;
    text-align: center;
  }
  .brand-name {
    margin: 0;
    font-family: "Lobster", cursive;
    font-weight: 400;
    font-size: 134px;
    line-height: 1;
    color: var(--brand-purple);
    white-space: nowrap;
  }
  .brand-name sup {
    font-size: 36px;
    vertical-align: top;
    position: relative;
    top: 16px;
    margin-left: 2px;
  }
  .product-type {
    margin: 8px 0 0;
    font-family: "Lobster", cursive;
    font-weight: 400;
    font-size: 54px;
    line-height: 1;
    color: var(--brand-cyan-deep);
  }
  .claims {
    margin: 34px 0 0;
    padding: 0;
    list-style: none;
    font-family: "Baloo 2", sans-serif;
    line-height: 1.05;
  }
  .claim-snip {
    font-size: 46px;
    font-weight: 800;
    color: var(--brand-purple);
    letter-spacing: 1px;
  }
  .claim-size {
    font-size: 24px;
    font-weight: 600;
    color: var(--brand-purple-deep);
    margin-top: 2px;
  }
  .claim-strength {
    font-size: 34px;
    font-weight: 700;
    color: var(--brand-cyan-deep);
    letter-spacing: 1px;
    margin-top: 14px;
  }
  .sheet-badge {
    position: absolute;
    left: -4px;
    top: 815px;
    width: 206px;
    height: 206px;
    border-radius: 50%;
    background: var(--brand-purple);
    border: 8px solid var(--badge-ring);
    box-sizing: border-box;
    display: flex;
    flex-direction: column;
    align-items: center;
    justify-content: center;
    color: #ffffff;
    font-family: "Baloo 2", sans-serif;
    font-weight: 700;
    line-height: 0.95;
    text-align: center;
  }
  .sheet-badge .count { font-size: 56px; }
  .sheet-badge .unit { font-size: 50px; }
  .eco-note {
    position: absolute;
    left: 640px;
    top: 1110px;
    width: 520px;
    margin: 0;
    text-align: center;
    font-family: "Baloo 2", sans-serif;
    font-weight: 700;
    font-size: 34px;
    line-height: 1;
    color: var(--brand-purple);
  }
</style>
</head>
<body>
  <main class="pack-front">
    <svg class="art-layer" width="1200" height="1200" viewBox="0 0 1200 1200">
      <defs>
        <linearGradient id="leafGrad" x1="0" y1="0" x2="1" y2="1">
          <stop offset="0" stop-color="#7d56ad"/>
          <stop offset="1" stop-color="#4e2f78"/>
        </linearGradient>
        <radialGradient id="floralGrad" cx="0.38" cy="0.4" r="0.72">
          <stop offset="0" stop-color="#fbee3e"/>
          <stop offset="0.55" stop-color="#c8e07a"/>
          <stop offset="1" stop-color="#33a6d7"/>
        </radialGradient>
        <radialGradient id="dragonflyGrad" cx="0.5" cy="0.45" r="0.6">
          <stop offset="0" stop-color="#fbee3e"/>
          <stop offset="1" stop-color="#fdf6a6" stop-opacity="0.2"/>
        </radialGradient>
      </defs>

      <line class="roll-seam" x1="600" y1="330" x2="600" y2="1200" stroke="var(--seam-grey)" stroke-width="6"/>

      <path class="leaf-pattern" role="img" aria-label="Decorative pattern of large leaves with white veins across the top of the pack"
            d="M300 0 H1200 V300 C1100 340 1000 290 900 320 C800 350 720 300 620 330 C540 355 460 330 400 360 C360 300 330 160 300 0 Z"
            fill="url(#leafGrad)"/>

      <path class="floral-cluster-top" role="img" aria-label="Cluster of yellow flowers and clover leaves in the top left corner"
            d="M0 0 H470 C450 80 500 150 430 210 C380 260 330 250 300 320 C260 400 170 420 110 470 C60 510 20 470 0 480 Z"
            fill="url(#floralGrad)"/>

      <path class="floral-cluster-bottom" role="img" aria-label="Cluster of yellow flowers and clover leaves in the bottom left corner"
            d="M0 700 C80 690 150 720 220 760 C300 800 400 850 420 950 C440 1050 370 1120 300 1200 H0 Z"
            fill="url(#floralGrad)"/>

      <ellipse class="dragonfly" role="img" aria-label="Small yellow dragonfly with a dotted flight trail"
               cx="930" cy="960" rx="105" ry="105" fill="url(#dragonflyGrad)"/>
    </svg>

    <div class="brand-block">
      <h1 class="brand-name">Floramist<sup>TM</sup></h1>
      <p class="product-type">Paper Towels</p>
      <ul class="claims">
        <li class="claim-snip">SNIP-N-WIPE</li>
        <li class="claim-size">11 in × 6 in sheets</li>
        <li class="claim-strength">STRONG &amp; ABSORBENT</li>
      </ul>
    </div>

    <div class="sheet-badge">
      <span class="count">100</span>
      <span class="unit">Sheets</span>
    </div>

    <p class="eco-note">100% Biodegradable</p>
  </main>
</body>
</html>
```